verdant manor grounds simple classy business card design

my name is owen brackley and I run a gardening business aimed at high class verdant manor grounds. the business name is verdant manor grounds and our logo was designed on brief hive .My clientel are anything from residential homes to businesses. I take pride in my work and know that I offer a service like no other in my area.
The business card will be used to represent my business and I want it to be not only rememberable, but simplistic and modern. Eye catching too. Of course I would like it relatable to gardening and appealing to the correct clientel - those being garden enthusiasts, prestigious homes and businesses that are after top of the line gardening services like no other on the market.
I am not a typical lawn mowing business so I don't want a typical card design that represents that. The gardens I work with are generally million dollar properties with owners who are very garden proud looking for upkeep and guidance from me along with sometimes whole new garden designs. I want the business cards to show to my clients that I take pride, as they do, in their garden. And I want them to know from my card that I am a professional, qualified horticulturist offering them a top of the line service for life. I want them to refer my business on. I want them to look at my business card and see class and professionalism in a modern unique bold way.
The card should be simple with the possibility of the logo on the front being embossed/debossed and my details on the back the card should have a organic garden feel it's very important to me that it is absolutely perfect
I am also very open to ideas and suggestions so look forward to seeing the designs. the business logo has been supplied with this project and I want the card to be double sided

Contact info is
Owen Brackley - Managing Director / Horticulturist
Phone : 0481 562 907
Email: owenbrackley@verdantmanorgrounds.example.au

Target Market(s)

high class gardens residential and commercial

Industry/Entity Type

Gardener

Contact Information for Business Card

Contact info is
Phone : 0481 562 907

PLEASE MAKE CARD DOUBLE SIDED

Requirements
Must have
• organic simple classy modern feel
• must flow with the current logo that has been supplied with this project
• Double sided
• Must explain in a simple way that I deal with high end gardens and I'm a qualified horticulturist
Nice to have
• embossed debossed logo
Should not have
• shouldn't be to busy or cheap looking

```html
<!DOCTYPE html>
<html lang="en">
<head>
<meta charset="utf-8">
<title>Verdant Manor Grounds – Business Card</title>
<link href="https://fonts.googleapis.com/css2?family=Source+Sans+3:wght@400;600&display=swap" rel="stylesheet">
<style>
  :root {
    --backdrop: #f1f1ef;
    --card-grey: #58585a;
    --gold: #d4a02a;
    --gold-light: #e8c35a;
    --leaf-green: #5f9f45;
    --sky: #2a6fb8;
    --hedge: #3f6a2a;
    --hedge-dark: #2c4a1d;
  }
  * { margin: 0; padding: 0; box-sizing: border-box; }
  html, body {
    width: 1200px; height: 854px; overflow: hidden;
    background: var(--backdrop);
    font-family: "Source Sans 3", sans-serif;
  }
  .canvas { position: relative; width: 1200px; height: 854px; }

  .card-back {
    position: absolute; left: 190px; top: 177px;
    width: 303px; height: 530px;
    background: var(--card-grey);
    text-align: center;
  }
  .brand-name {
    color: var(--leaf-green);
    font-weight: 600;
    text-transform: uppercase;
    letter-spacing: 3px;
    line-height: 1.25;
  }
  .card-back .brand-name {
    position: absolute; left: 0; right: 0; top: 142px;
    font-size: 24px;
  }
  .gold-rule {
    position: absolute; height: 4px;
    background: linear-gradient(90deg, var(--gold), var(--gold-light), var(--gold));
  }
  .card-back .gold-rule { left: 25px; width: 252px; top: 271px; }
  .holder-name {
    position: absolute; left: 0; right: 0; top: 318px;
    color: var(--gold); font-size: 25px; font-weight: 400;
  }
  .holder-role {
    position: absolute; left: 0; right: 0; top: 361px;
    color: var(--gold); font-size: 13.5px;
  }
  .contact {
    position: absolute; left: 0; right: 0; top: 432px;
    color: var(--gold); font-size: 11.5px; line-height: 18px;
  }

  .card-front {
    position: absolute; left: 560px; top: 278px;
    width: 529px; height: 302px;
    background: var(--card-grey);
    padding: 5px 5px 10px;
  }
  .garden-photo {
    width: 100%; height: 100%;
    background: linear-gradient(180deg, var(--sky) 0%, #d9c7a6 22%, #c9b89a 36%, #7aa04a 46%, var(--hedge) 70%, var(--hedge-dark) 92%, #8a8c86 100%);
  }
  .front-panel {
    position: absolute; left: 171px; top: 0;
    width: 174px; height: 109px;
    background: var(--card-grey);
    border-radius: 0 0 6px 6px;
    text-align: center;
  }
  .front-panel .brand-name {
    position: absolute; left: 0; right: 0; top: 42px;
    font-size: 13px; letter-spacing: 2px;
  }
  .front-panel .gold-rule { left: 8px; width: 156px; top: 103px; height: 2px; }
</style>
</head>
<body>
<main class="canvas">
  <section class="card-back" aria-label="Card back with contact details">
    <div class="brand-name">Verdant Manor<br>Grounds</div>
    <div class="gold-rule"></div>
    <h1 class="holder-name">Owen Brackley</h1>
    <p class="holder-role">Managing Director / Horticulturist</p>
    <p class="contact">Phone : 0481 562 907<br>Email: owenbrackley@verdantmanorgrounds.example.au</p>
  </section>

  <section class="card-front" aria-label="Card front">
    <div class="garden-photo" role="img" aria-label="Photograph of a formal manor garden with clipped hedges, stone steps and a brick chateau under blue sky"></div>
    <div class="front-panel">
      <div class="brand-name">Verdant Manor<br>Grounds</div>
      <div class="gold-rule"></div>
    </div>
  </section>
</main>
</body>
</html>
```